Geschäftspapiere für moderne Handwerksfirma
Zielgruppe
Wir sind eine moderne Handwerksfirma im Bereich Elektrotechnik und erneuerbare Energie. Unsere Zielgruppe sind Privatpersonen, Kommunen, Firmen, Landwirtschaften
Aufgabenstellung
Unser Design soll unser Logo, sowie unsere Hauptfarben anthrazit und rot aufweisen.

```html
<!DOCTYPE html>
<html lang="de">
<head>
<meta charset="utf-8">
<title>Brant Energie – Geschäftsausstattung</title>
<link href="https://fonts.googleapis.com/css2?family=Open+Sans:wght@400;600;700&family=Open+Sans+Condensed:wght@700&display=swap" rel="stylesheet">
<style>
  :root {
    --red: #d0091e;
    --dark-red: #8e0b17;
    --anthracite: #3f4647;
    --ink: #3a3a3a;
    --paper: #ffffff;
    --stage: #d9d8d6;
    --faint: #f1f1f1;
    --line: #c8c8c8;
  }
  * { margin: 0; padding: 0; box-sizing: border-box; }
  html, body { width: 1200px; height: 826px; overflow: hidden; }
  body { background: var(--stage); font-family: "Open Sans", Arial, sans-serif; color: var(--ink); position: relative; }
  .sheet { position: absolute; background: var(--paper); box-shadow: 4px 5px 10px rgba(0,0,0,.25); overflow: hidden; }
  .icons { position: absolute; width: 0; height: 0; }

  .brand { position: absolute; display: flex; align-items: center; gap: 6px; }
  .brand-dot { border-radius: 50%; background: var(--red); flex: none; }
  .brand-name { color: var(--red); font-weight: 700; line-height: .95; letter-spacing: .5px; }

  .contact-list { list-style: none; }
  .contact-list li { display: flex; align-items: center; gap: 5px; white-space: nowrap; }
  .contact-list svg { width: 7px; height: 7px; fill: var(--red); flex: none; }

  /* Briefbogen */
  .letterhead { left: 36px; top: 30px; width: 536px; height: 758px; }
  .letterhead .bands { position: absolute; left: 0; width: 536px; }
  .letterhead .bands-top { top: 0; height: 14px; }
  .letterhead .bands-bottom { bottom: 0; height: 14px; }
  .letterhead .brand { left: 63px; top: 24px; }
  .letterhead .brand-dot { width: 42px; height: 42px; }
  .letterhead .brand-name { font-size: 25px; }
  .letterhead .sender-block { position: absolute; left: 406px; top: 31px; font-size: 7px; line-height: 10px; color: var(--red); font-weight: 700; }
  .letterhead .contact-list { position: absolute; left: 406px; top: 72px; font-size: 7px; line-height: 10px; }
  .letterhead .return-line { position: absolute; left: 63px; top: 116px; font-family: "Open Sans Condensed", "Open Sans", sans-serif; font-weight: 700; font-size: 5.5px; color: var(--ink); }
  .letterhead .return-line .sep { color: var(--red); margin: 0 3px; }
  .fold-mark { position: absolute; left: 0; height: 1px; background: var(--line); }
  .watermark { position: absolute; left: 286px; top: 406px; width: 220px; height: 220px; border-radius: 50%; background: var(--faint); }
  .footer { position: absolute; top: 711px; left: 63px; right: 20px; font-size: 6px; line-height: 10px; }
  .footer .col { position: absolute; top: 0; white-space: nowrap; }
  .footer .label { color: var(--red); font-weight: 700; }
  .footer .contact-list svg { width: 6px; height: 6px; }

  /* Umschlag */
  .envelope { left: 601px; top: 111px; width: 563px; height: 281px; }
  .envelope .brand { left: 50px; top: 38px; }
  .envelope .brand-dot { width: 38px; height: 38px; }
  .envelope .brand-name { font-size: 22px; }
  .envelope .sender-block { position: absolute; left: 218px; top: 54px; font-size: 7px; line-height: 10px; font-weight: 700; color: #111; }
  .envelope .window { position: absolute; left: 52px; top: 127px; width: 230px; height: 115px; border: 1px solid var(--line); border-radius: 8px; }

  /* Visitenkarte */
  .card-front { left: 773px; top: 449px; width: 217px; height: 140px; }
  .card-front .brand { left: 13px; top: 13px; }
  .card-front .brand-dot { width: 26px; height: 26px; }
  .card-front .brand-name { font-size: 15px; }
  .card-front .person { position: absolute; left: 13px; top: 66px; font-size: 8px; }
  .card-front .person .role { color: var(--red); font-weight: 700; }
  .card-front .sender-block { position: absolute; left: 13px; top: 93px; font-size: 6px; line-height: 10px; font-weight: 700; color: #111; }
  .card-front .contact-list { position: absolute; left: 104px; top: 93px; font-size: 6px; line-height: 9px; }
  .card-front .contact-list svg { width: 6px; height: 6px; }
  .card-front .bands { position: absolute; left: 0; bottom: 0; width: 217px; height: 12px; }

  .card-back { left: 773px; top: 603px; width: 217px; height: 140px; background: var(--red); }
  .card-back .emblem { position: absolute; left: 80px; top: 24px; width: 58px; height: 58px; border-radius: 50%; background: var(--dark-red); }
  .card-back .url { position: absolute; left: 0; right: 0; top: 115px; text-align: center; font-size: 9px; font-weight: 700; color: var(--dark-red); }
</style>
</head>
<body>

<svg class="icons" aria-hidden="true">
  <defs>
    <symbol id="i-phone" viewBox="0 0 10 10"><path d="M2 0.5 L3.6 0.5 L4.2 2.8 L3.1 3.6 C3.6 4.8 5 6.3 6.4 6.9 L7.2 5.8 L9.5 6.4 L9.5 8 C9.5 9 8.8 9.5 8 9.5 C4 9.2 0.8 6 0.5 2 C0.5 1.2 1 0.5 2 0.5Z"/></symbol>
    <symbol id="i-fax" viewBox="0 0 10 10"><path d="M2.5 0.5h5v3h-5z M1 4h8c.6 0 1 .4 1 1v3.5H8.5v1h-7v-1H0V5c0-.6.4-1 1-1z M2.5 6.5v2h5v-2z" fill-rule="evenodd"/></symbol>
    <symbol id="i-mail" viewBox="0 0 10 10"><path d="M0 2h10v6H0z M0.6 2.4 L5 5.6 L9.4 2.4" /><path d="M0.8 2.6 L5 5.5 L9.2 2.6" fill="none" stroke="#fff" stroke-width=".8"/></symbol>
    <symbol id="i-web" viewBox="0 0 10 10"><path d="M5 0a5 5 0 1 0 0.01 0z M5 1.1a3.9 3.9 0 1 1-0.01 0z" fill-rule="evenodd"/><path d="M5 1v8 M1 5h8 M1.6 3h6.8 M1.6 7h6.8 M5 1c-2.2 2.2-2.2 5.8 0 8 M5 1c2.2 2.2 2.2 5.8 0 8" fill="none" stroke="currentColor" stroke-width=".7"/></symbol>
  </defs>
</svg>

<!-- Briefbogen -->
<section class="sheet letterhead">
  <svg class="bands bands-top" viewBox="0 0 536 14" preserveAspectRatio="none" aria-hidden="true">
    <path d="M0 0H378C382 0 384 3 386 7H0Z" fill="var(--red)"/>
    <path d="M388 0H536V14H398C394 14 392 6 388 0Z" fill="var(--anthracite)"/>
  </svg>

  <div class="brand">
    <span class="brand-dot"></span>
    <span class="brand-name">BRANT<br>ENERGIE</span>
  </div>

  <p class="sender-block">Brant - Energie GmbH<br>Am Lindenweg 12<br>87654 Tannried</p>
  <ul class="contact-list">
    <li><svg><use href="#i-phone"/></svg>08341/55210-0</li>
    <li><svg><use href="#i-fax"/></svg>08341/55210-99</li>
    <li><svg><use href="#i-mail"/></svg>info@brant-energie.de</li>
    <li><svg style="color:var(--red)"><use href="#i-web"/></svg>www.brant-energie.de</li>
  </ul>

  <p class="return-line">Brant - Energie GmbH<span class="sep">|</span>Am Lindenweg 12<span class="sep">|</span>87654 Tannried</p>

  <span class="fold-mark" style="top:224px;width:18px"></span>
  <span class="fold-mark" style="top:382px;width:26px"></span>
  <span class="fold-mark" style="top:494px;width:18px"></span>

  <div class="watermark" aria-hidden="true"></div>

  <footer class="footer">
    <div class="col" style="left:0"><span class="label">Brant - Energie GmbH<br>Am Lindenweg 12<br>87654 Tannried</span></div>
    <div class="col" style="left:92px"><span class="label">Geschäftsführer:</span><br>Jonas Brant</div>
    <ul class="col contact-list" style="left:164px">
      <li><svg><use href="#i-phone"/></svg>08341/55210-0</li>
      <li><svg><use href="#i-fax"/></svg>08341/55210-99</li>
      <li><svg><use href="#i-mail"/></svg>info@brant-energie.de</li>
      <li><svg style="color:var(--red)"><use href="#i-web"/></svg>www.brant-energie.de</li>
    </ul>
    <div class="col" style="left:258px"><span class="label">Amtsgericht:</span><br>Kaufbeuren HRB 20415<br>UST-ID: DE-512093377</div>
    <div class="col" style="left:343px"><span class="label">Bankverbindung:</span><br>Raiffeisenbank Tannried-Allgäu<br>IBAN: DE12 3456 7800 0009 8765 43<br>BIC: GENODEF1TNR</div>
  </footer>

  <svg class="bands bands-bottom" viewBox="0 0 536 14" preserveAspectRatio="none" aria-hidden="true">
    <path d="M0 0H140C144 0 146 8 150 14H0Z" fill="var(--anthracite)"/>
    <path d="M150 7H536V14H154C152 11 151 9 150 7Z" fill="var(--red)"/>
  </svg>
</section>

<!-- Umschlag -->
<section class="sheet envelope">
  <div class="brand">
    <span class="brand-dot"></span>
    <span class="brand-name">BRANT<br>ENERGIE</span>
  </div>
  <p class="sender-block">Brant - Energie GmbH<br>Am Lindenweg 12<br>87654 Tannried</p>
  <div class="window"></div>
</section>

<!-- Visitenkarte Vorderseite -->
<section class="sheet card-front">
  <div class="brand">
    <span class="brand-dot"></span>
    <span class="brand-name">BRANT<br>ENERGIE</span>
  </div>
  <p class="person">Jonas Brant - <span class="role">Geschäftsführer</span></p>
  <p class="sender-block">Brant - Energie GmbH<br>Am Lindenweg 12<br>87654 Tannried</p>
  <ul class="contact-list">
    <li><svg><use href="#i-phone"/></svg>08341/55210-0</li>
    <li><svg><use href="#i-fax"/></svg>08341/55210-99</li>
    <li><svg><use href="#i-mail"/></svg>jonasbrant@brant-energie.de</li>
    <li><svg style="color:var(--red)"><use href="#i-web"/></svg>www.brant-energie.de</li>
  </ul>
  <svg class="bands" viewBox="0 0 217 12" preserveAspectRatio="none" aria-hidden="true">
    <path d="M0 0H76C78 0 79 6 82 12H0Z" fill="var(--anthracite)"/>
    <path d="M82 6H217V12H84C83 10 82 8 82 6Z" fill="var(--red)"/>
  </svg>
</section>

<!-- Visitenkarte Rückseite -->
<section class="sheet card-back">
  <div class="emblem" aria-hidden="true"></div>
  <p class="url">www.brant-energie.de</p>
</section>

</body>
</html>
```